We use a logo that is a sort of smiley face. The mouth is a wrench curved to make the smile. One end of the wrench is a box end and the other is an open end. (These are types of wrenches. If you google combination wrench it will show you) The for the eyes they are hex shaped like nuts (six sides). We want to use this logo and our information for a letterhead that we will use to print invoices. The top right corner needs to have a clean area for the invoice number.
Steadfield Automotive Repair
and Maintenance
48307 Talmin Dr.
Austin, TX 78729
512-608-4197
www.steadfieldautofix.example
If you can design this information plus the smiley face on there somewhere.
Automotive
Steadfield Automotive Repair and Maintenance

```html
<!DOCTYPE html>
<html lang="en">
<head>
<meta charset="utf-8">
<title>Steadfield Automotive Repair and Maintenance — Letterhead</title>
<link rel="stylesheet" href="https://fonts.googleapis.com/css2?family=Noto+Serif:wght@400;700&display=swap">
<style>
  :root {
    --paper: #ffffff;
    --ink: #111111;
    --brand-yellow: #f2ea00;
    --brand-yellow-light: #fbf66a;
  }
  html, body {
    margin: 0;
    padding: 0;
    overflow: hidden;
    background: var(--paper);
  }
  .letterhead {
    position: relative;
    width: 1200px;
    height: 400px;
    background: var(--paper);
    font-family: "Noto Serif", Georgia, serif;
    color: var(--ink);
    overflow: hidden;
  }
  .brand {
    position: absolute;
    left: 62px;
    top: 126px;
    width: 218px;
    display: flex;
    flex-direction: column;
    align-items: center;
  }
  .brand-mark {
    display: block;
    width: 110px;
    height: 110px;
    margin-left: -7px;
  }
  .brand-name {
    margin-top: 16px;
    font-size: 10px;
    font-weight: 700;
    line-height: 1.2;
    white-space: nowrap;
    color: var(--ink);
  }
  .contact {
    position: absolute;
    left: 822px;
    top: 122px;
    margin: 0;
    font-size: 20px;
    font-weight: 400;
    line-height: 25.6px;
    font-style: normal;
    white-space: nowrap;
  }
</style>
</head>
<body>
  <main class="letterhead">
    <div class="brand">
      <svg class="brand-mark" viewBox="0 0 110 110" aria-hidden="true">
        <defs>
          <radialGradient id="mark-fill" cx="45%" cy="40%" r="60%">
            <stop offset="0" stop-color="var(--brand-yellow-light)"/>
            <stop offset="1" stop-color="var(--brand-yellow)"/>
          </radialGradient>
        </defs>
        <circle cx="55" cy="55" r="55" fill="url(#mark-fill)"/>
      </svg>
      <span class="brand-name">Steadfield Automotive Repair and Maintenance</span>
    </div>

    <address class="contact">
      Steadfield Automotive Repair<br>
      and Maintenance<br>
      48307 Talmin Dr.<br>
      Austin, TX 78729<br>
      512-608-4197<br>
      www.steadfieldautofix.example
    </address>
  </main>
</body>
</html>
```